Business Card Re-Design/Update

We'd like to update out business cards. I've included our current "Style guide" which has the colour scheme of the organisation in it. I've also included the branding files with logos etc in them.

I've also included a copy of one of our existing cards so that you can see how ugly/dated they look. I'd like a fresh modern corporate look.

Target Market(s)

These are for our clients, potential clients, industry contacts - like all business cards

Contact Information for Business Card

Name
Position
Company Address - Level 1, 47 Garnet Lane, Toowong Qld 4066
Direct Phone
mobile
Email
Website -www.korvalnet.com.au
Logo

Colors

Designer to choose colors to be used in the design.

Requirements
Must have
• Main Logo
• Cards will need to be editable to be able to personalize them for each new employee.
Nice to have
• The MapOUT, HandOVER, UpKEEP would be okay to have if they can be sensibly and professionally added to the look without detracting from the main imagery.
• Maybe they could go on the back of the card? will leave this to your creative discretion as to whether/where they fit.
Should not have
• Should not have decorative or script fonts

```html
<!DOCTYPE html>
<html lang="en">
<head>
<meta charset="utf-8">
<title>korvalnet business card</title>
<link rel="stylesheet" href="https://fonts.googleapis.com/css2?family=Work+Sans:wght@400;500;600&display=swap">
<style>
  :root {
    --backdrop: #4a403b;
    --card: #1c1c1d;
    --card-edge: #b3141c;
    --red: #e3212b;
    --white: #f4f4f4;
    --muted: #d9d9d9;
  }
  * { box-sizing: border-box; margin: 0; padding: 0; }
  html, body { width: 1200px; height: 715px; overflow: hidden; }
  body {
    background: var(--backdrop);
    font-family: "Work Sans", Arial, sans-serif;
    position: relative;
  }
  .card {
    position: absolute;
    top: 208px;
    width: 525px;
    height: 300px;
    background: var(--card);
    border-radius: 4px;
    box-shadow: 0 6px 18px rgba(0,0,0,.35);
  }
  .card--front { left: 50px; border-bottom: 4px solid var(--card-edge); }
  .card--back { left: 625px; }
  .wordmark {
    position: absolute;
    display: flex;
    align-items: center;
    gap: 12px;
    color: var(--white);
    font-weight: 500;
    letter-spacing: .5px;
  }
  .wordmark__square { background: var(--red); flex: none; }
  .card--front .wordmark { left: 50%; top: 50%; transform: translate(-50%, -50%); font-size: 56px; }
  .card--front .wordmark__square { width: 34px; height: 34px; }
  .card--back .wordmark { left: 34px; top: 120px; font-size: 30px; gap: 8px; }
  .card--back .wordmark__square { width: 20px; height: 20px; }
  .divider {
    position: absolute;
    left: 246px; top: 50px;
    width: 2px; height: 200px;
    background: var(--red);
  }
  .details { position: absolute; left: 264px; top: 50px; right: 18px; color: var(--white); }
  .details__name { color: var(--red); font-size: 20px; font-weight: 600; text-transform: uppercase; letter-spacing: .5px; }
  .details__role { font-size: 12.5px; color: var(--muted); margin-bottom: 10px; }
  .details__address { font-size: 12.5px; line-height: 1.35; margin-bottom: 8px; }
  .contact { list-style: none; font-size: 12.5px; line-height: 1.5; }
  .contact li { display: flex; align-items: center; gap: 7px; }
  .contact svg { width: 9px; height: 9px; flex: none; fill: var(--red); }
</style>
</head>
<body>
  <section class="card card--front">
    <div class="wordmark"><span class="wordmark__square"></span>korvalnet</div>
  </section>

  <section class="card card--back">
    <div class="wordmark"><span class="wordmark__square"></span>korvalnet</div>
    <div class="divider"></div>
    <div class="details">
      <p class="details__name">Mara Ellison</p>
      <p class="details__role">Business Development Manager</p>
      <p class="details__address">12/58 Kestrel Road,<br>Newmarket QLD 4051</p>
      <ul class="contact">
        <li><svg viewBox="0 0 10 10"><rect x="2" y="0" width="6" height="10" rx="1"/></svg>+61 (0)491 570 159</li>
        <li><svg viewBox="0 0 10 10"><path d="M2 0l2 2-1 2q1 2 3 3l2-1 2 2-2 2Q3 9 0 2z"/></svg>+61 (0)7 5550 1316</li>
        <li><svg viewBox="0 0 10 10"><rect x="0" y="3" width="10" height="7"/><rect x="2" y="0" width="6" height="3"/></svg>+61 (0)7 5550 1333</li>
        <li><svg viewBox="0 0 10 10"><path d="M0 2h10v7H0zM0 2l5 4 5-4" fill="none" stroke="#e3212b" stroke-width="1.3"/></svg>+61 (0)7 5550 1303</li>
        <li><svg viewBox="0 0 10 10"><circle cx="5" cy="5" r="4.3" fill="none" stroke="#e3212b" stroke-width="1.3"/></svg>mellison@korvalnet.com.au</li>
        <li><svg viewBox="0 0 10 10" style="visibility:hidden"><circle cx="5" cy="5" r="4"/></svg>www.korvalnet.com.au</li>
      </ul>
    </div>
  </section>
</body>
</html>
```